Non-profit organisation for street children in Indonesia

Lentera Bocah provides home, education, family and health care for street children and other underprivileged children in Indonesia.

We need an emotional catchy advertisement that will make people aware of the terrible living conditions of street children in Indonesia and the great work the Lentera Bocah Foundation is doing to help these children.

We have 1 photo available for this advertisement. A little girl laying in the streets. This photo can be used with a strong quote such as "Street children whose responsibility?" or "Safer out on streets than at home" or "This child doesn't have the right to have a childhood worth remembering?" or another strong quote. Be creative! It need to touch people!

See some similar advertisements of other non-profit organizations what we very much like:

http://7brightpix.example/wp-content/uploads/2011/07/boldposters41.jpg
http://7brightpix.example/wp-content/uploads/2011/07/affiches-nobles-motifs-058.jpg

Mission
To give every child in the world the opportunity to live a happy and healthy life free of poverty, exploitation, and violence.

Overview
Lentera Bocah Foundation is an independent non-governmental organisation founded in 2005 in the Netherlands and expanded to Indonesia in 2006. Our aim is to improve the lives of children and to protect their rights by providing education, accommodation, family care and medical and legal aid.

Description
Lentera Bocah (Light for Youngsters) Foundation serves homeless and impoverished children by offering them a new path in life. By providing them with the necessary shelter, education, and psychological support directed towards vocational training, mentorship, and micro-credit opportunities, it strives to enable their re-entery into the community as happy and self-sufficient adults.

Facts:
There are 70 million children in Indonesia, nearly 18 million are very poor and estimated 170,000 children live on the streets.

Pitch submissions need to be 960x696 pixels.

Files available 1 photo and logo
Updates

Reason: Dear Designers, We have decided to extend the deadline because we haven't received what we are after. Please make a design in the trend as the following two examples: http://7brightpix.example/wp-content/uploads/2011/07/boldposters41.jpg http://7brightpix.example/wp-content/uploads/2011/07/affiches-nobles-motifs-058.jpg We hope to receive a good design shortly! Thank you Kind regards Lentera Bocah

Target Market(s)

Everybody

Industry/Entity Type

Non-Profit

Requirements
Must have
• 1. A strong quote.
2. Website url: www.lenterabocah.org
3. Mission quote from Lentera Bocah:
Should not have
• To much text.

```html
<!DOCTYPE html>
<html lang="en">
<head>
<meta charset="utf-8">
<title>Lentera Bocah Foundation</title>
<link rel="stylesheet" href="https://fonts.googleapis.com/css2?family=Tinos:ital,wght@0,400;0,700;1,400&display=swap">
<style>
  :root {
    --page: #ffffff;
    --road-dark: #151517;
    --road-mid: #2f3033;
    --road-light: #4a4b4f;
    --pavement: #6b4a4c;
    --kerb: #8c8c8a;
    --accent: #e3161b;
    --body-text: #f2f2f2;
    --quote-text: #ffffff;
    --badge-fill: #e6e6e6;
    --badge-frame: #ffffff;
  }
  * { margin: 0; padding: 0; box-sizing: border-box; }
  html, body {
    width: 1200px; height: 889px; overflow: hidden;
    background: var(--page);
  }
  .poster {
    position: relative;
    width: 1200px; height: 889px;
    background: var(--page);
    font-family: "Tinos", "Times New Roman", serif;
  }
  .street-photo {
    position: absolute;
    left: 54px; top: 53px;
    width: 1101px; height: 789px;
    background:
      linear-gradient(180deg, rgba(10,10,12,0.85) 0px, rgba(10,10,12,0.85) 70px, transparent 90px),
      radial-gradient(ellipse 380px 260px at 470px 500px, rgba(200,60,60,0.28), transparent 70%),
      linear-gradient(108deg, transparent 0%, transparent 47%, rgba(140,140,138,0.35) 50%, transparent 54%),
      radial-gradient(ellipse 560px 640px at 120px 620px, var(--pavement), transparent 75%),
      linear-gradient(180deg, var(--road-dark) 0%, var(--road-mid) 45%, var(--road-light) 100%);
  }
  .street-photo::after {
    content: "";
    position: absolute; inset: 0;
    background: radial-gradient(ellipse 900px 620px at 50% 50%, transparent 55%, rgba(0,0,0,0.55) 100%);
  }
  .badge {
    position: absolute;
    left: 157px; top: 134px;
    width: 174px; height: 232px;
    background: var(--badge-fill);
    border: 8px solid var(--badge-frame);
    display: flex; align-items: center; justify-content: center;
    text-align: center;
  }
  .badge-name {
    color: var(--accent);
    font-weight: 700;
    font-size: 26px;
    line-height: 1.1;
  }
  .info {
    position: absolute;
    left: 684px;
    width: 460px;
    color: var(--body-text);
    font-size: 18.5px;
    line-height: 21.5px;
  }
  .info-heading {
    color: var(--accent);
    font-weight: 400;
    font-size: 18.5px;
    line-height: 21.5px;
  }
  .mission { top: 139px; }
  .overview { top: 266px; }
  .description { top: 432px; }
  .facts { top: 643px; }
  .headline {
    position: absolute;
    left: 100px; top: 716px;
    width: 520px;
    color: var(--quote-text);
    font-weight: 700;
    font-size: 34px;
    line-height: 38px;
  }
  .headline em {
    color: var(--accent);
    font-style: normal;
  }
  .site-url {
    position: absolute;
    left: 684px; top: 790px;
    color: var(--accent);
    font-weight: 700;
    font-size: 20px;
    line-height: 22px;
  }
</style>
</head>
<body>
<main class="poster">
  <div class="street-photo" role="img" aria-label="Photograph of a little girl lying curled on the kerb of a paved city street"></div>

  <div class="badge">
    <span class="badge-name">Lentera<br>Bocah</span>
  </div>

  <section class="info mission">
    <h2 class="info-heading">Mission</h2>
    <p>To give every child in the world the<br>opportunity to live a happy and<br>healthy life free of poverty, exploitation,<br>and violence.</p>
  </section>

  <section class="info overview">
    <h2 class="info-heading">Overview</h2>
    <p>Lentera Bocah Foundation is an independent<br>non-governmental organisation founded in 2005 in<br>the Netherlands and expanded to Indonesia in 2006.<br>Our aim is to improve the lives of children and to<br>protect their rights by providing education,<br>accommodation, family care &amp; medical &amp; legal aid.</p>
  </section>

  <section class="info description">
    <h2 class="info-heading">Description</h2>
    <p>Lentera Bocah (Light for Youngsters) Foundation serves<br>homeless &amp; impoverished children by offering them<br>a new path in life. By providing them with the<br>necessary shelter, education, and psychological<br>support directed towards vocational training,<br>mentorship, &amp; micro-credit opportunities, it strives<br>tenable their re-entery into the community as<br>happy and self-sufficient adults.</p>
  </section>

  <section class="info facts">
    <h2 class="info-heading">Facts</h2>
    <p>There are 70 million children in<br>Indonesia, nearly 18 million are very<br>poor and estimated 170,000 children<br>live on the streets.</p>
  </section>

  <h1 class="headline">Street children.<br><em>Whose responsibility?</em></h1>

  <p class="site-url">www.lenterabocah.org</p>
</main>
</body>
</html>
```